Hollowbrook Renderworks Wordpress Design

I would like a design for my friends company. He has just had his logo designed and really likes the following website.

www.tbr-skimcoat.co.uk

Something similar to this design would be ideal but open to additional ideas. The website shown has all the relevant content.

We have 20 years of experience and can provide a number of photos for work we have done.

More photos will be provided upon request.

Target Market(s)

Homeowners

Industry/Entity Type

Trade

Font styles to use
Sans Serif

Colors
3176b5
85cae6
85abd2
eaf1f7

Requirements
Must have
• look at www.tbr-skimcoat.co.uk
Nice to have
Should not have
• N/A

```html
<!DOCTYPE html>
<html lang="en">
<head>
<meta charset="utf-8">
<title>Hollowbrook Renderworks</title>
<link href="https://fonts.googleapis.com/css2?family=Open+Sans:ital,wght@0,400;0,600;0,700;1,400&family=Raleway:wght@400;500;600;700&family=Tinos&display=swap" rel="stylesheet">
<style>
:root{
  --blue:#3176b5;
  --blue-deep:#1f5aa3;
  --sky:#85cae6;
  --steel:#85abd2;
  --mist:#eaf1f7;
  --navy:#0c3f86;
  --navy-dark:#0a2f66;
  --ink:#333a42;
  --muted:#6b7480;
  --white:#ffffff;
  --send:#2f80e0;
}
*{margin:0;padding:0;box-sizing:border-box}
html,body{width:1200px;height:2765px;overflow:hidden;background:var(--white)}
body{position:relative;font-family:"Open Sans",Arial,sans-serif;color:var(--ink)}
h2{font-weight:400}
.abs{position:absolute}

/* header */
.site-header{left:0;top:0;width:1200px;height:122px;background:var(--white)}
.brand{left:160px;top:34px;display:flex;align-items:center;gap:12px}
.brand-mark{width:22px;height:22px;background:var(--blue)}
.brand-name{font-family:"Raleway",sans-serif;font-weight:700;font-size:30px;color:var(--blue);letter-spacing:1px}
.phone{left:876px;top:30px;display:flex;align-items:center;gap:10px;font-family:"Raleway",sans-serif;font-size:24px;color:#3a3f46}
.phone-icon{width:30px;height:30px;border-radius:50%;background:var(--blue);display:flex;align-items:center;justify-content:center}
.search{left:814px;top:70px;width:232px;height:34px;border:1px solid #cfd3d8;background:#fafafa;font-size:11px;color:#9aa0a6;padding:9px 12px}
.search svg{position:absolute;right:10px;top:8px}

/* nav */
.main-nav{left:0;top:122px;width:1200px;height:50px;background:linear-gradient(#9cbde2,#6f9bcf)}
.main-nav ul{list-style:none;position:absolute;left:155px;top:0;display:flex;height:50px}
.main-nav li{height:50px;line-height:50px;color:var(--white);font-size:15px;text-align:center;border-right:1px solid rgba(255,255,255,.35)}
.main-nav li.active{background:var(--blue-deep)}

/* hero */
.hero{left:0;top:172px;width:1200px;height:484px;background:linear-gradient(180deg,#cfd6dc 0%,#8e8f90 45%,#5c4a44 100%)}
.hero-title{left:0;top:150px;width:1200px;text-align:center;color:var(--white);font-family:"Raleway",sans-serif;font-weight:600;font-size:66px;letter-spacing:1px;text-shadow:0 2px 6px rgba(0,0,0,.4)}
.hero-sub{left:0;top:240px;width:1200px;text-align:center;color:var(--white);font-family:"Raleway",sans-serif;font-weight:600;font-size:36px;text-shadow:0 2px 6px rgba(0,0,0,.4)}
.hero-arrow{top:190px}

/* about */
.about{left:0;top:656px;width:1200px;height:315px;text-align:center}
.about-title{left:0;top:78px;width:1200px;font-family:"Tinos",serif;font-weight:400;font-size:31px;color:#333;letter-spacing:.5px}
.about-lead{left:0;top:138px;width:1200px;font-size:13.5px;color:var(--muted)}
.about-body{left:158px;top:174px;width:884px;font-size:13.5px;line-height:24px;color:var(--muted)}

/* services */
.services{left:0;top:971px;width:1200px;height:315px;background:linear-gradient(135deg,#3a85c6 0%,#2f6fb3 50%,#1f5aa3 100%)}
.service{top:50px;width:300px;text-align:center;color:var(--white)}
.service-ring{width:114px;height:114px;border:3px solid var(--white);border-radius:50%;margin:0 auto;display:flex;align-items:center;justify-content:center}
.service-name{font-family:"Raleway",sans-serif;font-weight:600;font-size:21px;margin-top:12px}
.service-text{font-size:11.5px;line-height:17px;margin-top:6px}

/* recent work */
.recent{left:0;top:1286px;width:1200px;height:440px;background:linear-gradient(180deg,#e9e6e1,#ece9e4)}
.recent-title{left:0;top:42px;width:1200px;text-align:center;font-family:"Raleway",sans-serif;font-weight:400;font-size:29px;color:var(--blue-deep)}
.recent-sub{left:0;top:86px;width:1200px;text-align:center;font-size:14px;color:#666}
.thumb{top:142px;width:215px;height:168px}
.thumb.t1{left:155px;background:linear-gradient(#8a9098,#5c6670);outline:3px solid var(--white);outline-offset:-6px}
.thumb.t2{left:378px;background:linear-gradient(#a8a196,#7a5a46)}
.thumb.t3{left:601px;background:linear-gradient(#b7b39f,#8a6a3e)}
.thumb.t4{left:824px;background:linear-gradient(#b5aba0,#6a5a4e)}

/* video */
.video-band{left:0;top:1630px;width:1200px;height:426px}
.video-title{left:170px;top:128px;font-family:"Raleway",sans-serif;font-weight:400;font-size:29px;color:var(--white)}
.video-lead{left:170px;top:182px;width:450px;font-size:14.5px;line-height:24px;color:var(--white)}
.video-body{left:170px;top:246px;width:450px;font-size:13px;line-height:22px;color:#eef6fb}
.player{left:649px;top:110px;width:398px;height:238px;background:linear-gradient(135deg,#dfe6ea,#9ea7ad 60%,#6f7a80)}
.player-bar{left:0;bottom:0;width:398px;height:26px;background:#2b2b2b}

/* testimonials */
.testimonials{left:0;top:2056px;width:1200px;height:336px;background:var(--mist)}
.test-title{left:0;top:50px;width:1200px;text-align:center;font-family:"Raleway",sans-serif;font-weight:400;font-size:27px;color:#333}
.avatar{left:226px;top:100px;width:178px;height:178px;border-radius:50%;background:linear-gradient(#c9c4bd,#b58e7a 60%,#d2284a)}
.quote-mark{font-family:"Tinos",serif;font-size:70px;color:var(--blue);line-height:1}
.quote-text{left:456px;top:120px;width:524px;font-style:italic;font-size:13px;line-height:27px;color:#555}
.quote-author{left:460px;top:220px;font-size:14px;font-weight:600;color:#333}
.quote-city{left:460px;top:245px;font-size:13px;color:#555}
.dots{left:574px;top:284px;display:flex;gap:3px}
.dot{width:13px;height:13px;border-radius:50%;background:var(--blue)}
.dot.open{background:transparent;border:2px solid var(--blue)}

/* footer */
.site-footer{left:0;top:2392px;width:1200px;height:373px;background:linear-gradient(180deg,#145aa8,#0c3f86 60%,#0a2f66)}
.f-head{font-family:"Raleway",sans-serif;font-size:19px;color:var(--white)}
.tweet{font-size:10px;line-height:16px;color:#dbe6f3;white-space:nowrap}
.tweet strong{display:block;font-size:12.5px;color:var(--white);font-weight:600}
.f-links{list-style:none;font-size:13px;line-height:30px;color:#e4ecf6}
.f-field{width:190px;height:30px;background:var(--white);font-size:10px;color:#777;padding:8px 10px;margin-bottom:6px}
.f-send{width:190px;height:30px;background:var(--send);color:var(--white);font-size:13px;font-weight:600;text-align:center;line-height:30px}
.contact-line{font-size:12.5px;line-height:30px;color:#e4ecf6;display:flex;align-items:center;gap:8px}
.contact-line.big{font-size:17px}
.socials{display:flex;gap:6px;margin-top:6px}
.social{width:30px;height:30px;border:2px solid var(--white);border-radius:50%}
.f-rule{left:158px;top:302px;width:884px;height:1px;background:rgba(255,255,255,.3)}
.copyright{left:158px;top:328px;font-size:11px;color:#cfdcee}
</style>
</head>
<body>

<header class="site-header abs">
  <div class="brand abs"><span class="brand-mark"></span><span class="brand-name">HOLLOWBROOK RENDERWORKS</span></div>
  <div class="phone abs">
    <span class="phone-icon"><svg width="16" height="16" viewBox="0 0 24 24"><path d="M6.6 10.8a15 15 0 0 0 6.6 6.6l2.2-2.2a1 1 0 0 1 1-.25 11.4 11.4 0 0 0 3.6.57 1 1 0 0 1 1 1V20a1 1 0 0 1-1 1A17 17 0 0 1 3 4a1 1 0 0 1 1-1h3.5a1 1 0 0 1 1 1c0 1.25.2 2.45.57 3.57a1 1 0 0 1-.25 1z" fill="#fff"/></svg></span>
    555-014-2387
  </div>
  <div class="search abs">Search here
    <svg width="16" height="16" viewBox="0 0 24 24"><circle cx="10" cy="10" r="6.5" fill="none" stroke="#9aa0a6" stroke-width="2.5"/><line x1="15" y1="15" x2="21" y2="21" stroke="#9aa0a6" stroke-width="2.5"/></svg>
  </div>
</header>

<nav class="main-nav abs">
  <ul>
    <li class="active" style="width:122px">HOME</li>
    <li style="width:138px">ABOUT US</li>
    <li style="width:132px">SERVICES</li>
    <li style="width:134px">PROJECTS</li>
    <li style="width:160px">TESTIMONIAL</li>
    <li style="width:156px;border-right:0">CONTACT US</li>
  </ul>
</nav>

<section class="hero abs" role="img" aria-label="Photo of a timber-framed house with white render panels">
  <div class="hero-title abs">PLASTERING SERVICES</div>
  <div class="hero-sub abs">MAURIS VEL LACUS VITAE FELIS</div>
  <svg class="hero-arrow abs" style="left:122px" width="22" height="36" viewBox="0 0 22 36"><polyline points="18,3 4,18 18,33" fill="none" stroke="#fff" stroke-width="4"/></svg>
  <svg class="hero-arrow abs" style="left:1052px" width="22" height="36" viewBox="0 0 22 36"><polyline points="4,3 18,18 4,33" fill="none" stroke="#fff" stroke-width="4"/></svg>
</section>

<section class="about abs">
  <h2 class="about-title abs">ABOUT HOLLOWBROOK RENDERWORKS</h2>
  <p class="about-lead abs">Mauris vel lacus vitae felis vestibulum volutpat imperdiet ac nisl Cum sociis natoque penatibus et magnis</p>
  <p class="about-body abs">Vivamus porttitor purus nisi eleifend libero a tempus libero lectus feugiat felis Morbi diam mauris viverra in gravida eu mattis in ante Morbi eget arcu Morbi porta libero id ullamcorper nonummy nibh ligula pulvinar metus eget consectetuer augue nisi quis lacus Ut ac mi quis lacus mollis aliquam Curabitur iaculis tempus eros Curabitur vel mi sit a</p>
</section>

<section class="services abs">
  <div class="service abs" style="left:150px">
    <div class="service-ring"><svg width="64" height="64" viewBox="0 0 64 64"><rect x="10" y="8" width="40" height="16" rx="3" fill="#fff"/><path d="M50 16h6v14H32v8" fill="none" stroke="#fff" stroke-width="4"/><rect x="28" y="38" width="8" height="20" rx="2" fill="#fff"/></svg></div>
    <div class="service-name">Plastering</div>
    <div class="service-text">Lorem ipsum dolor sit amet consectetuer<br>adipiscing elit Nam cursus Morbi ut mi</div>
  </div>
  <div class="service abs" style="left:449px">
    <div class="service-ring"><svg width="64" height="64" viewBox="0 0 64 64"><path d="M44 10a10 10 0 0 0-12 12L12 42a5 5 0 0 0 7 7l20-20a10 10 0 0 0 12-12l-6 6-6-2-2-6z" fill="#fff"/></svg></div>
    <div class="service-name">Repair Services</div>
    <div class="service-text">Lorem ipsum dolor sit amet consectetuer<br>adipiscing elit Nam cursus Morbi ut mi</div>
  </div>
  <div class="service abs" style="left:738px">
    <div class="service-ring"><svg width="64" height="64" viewBox="0 0 64 64"><g fill="#fff"><rect x="26" y="14" width="16" height="9"/><rect x="44" y="14" width="14" height="9"/><rect x="26" y="26" width="8" height="9"/><rect x="36" y="26" width="22" height="9"/><rect x="26" y="38" width="16" height="9"/><rect x="44" y="38" width="14" height="9"/><path d="M14 50c-6-4-6-12 0-20 0 6 4 6 4 2 4 4 6 12 0 18z"/></g></svg></div>
    <div class="service-name">Wall Insulation</div>
    <div class="service-text">Lorem ipsum dolor sit amet consectetuer<br>adipiscing elit Nam cursus Morbi ut mi</div>
  </div>
</section>

<section class="recent abs" role="img" aria-label="Faded photo of a plasterer at work behind the recent work gallery">
  <h2 class="recent-title abs">Our Recent Work</h2>
  <p class="recent-sub abs">Mauris vel lacus vitae felis vestibulum volutpat imperdiet ac nisl Cum sociis natoque penatibus</p>
  <div class="thumb t1 abs" role="img" aria-label="Photo of a rendered family house">
    <svg class="abs" style="left:88px;top:64px" width="38" height="38" viewBox="0 0 38 38"><circle cx="15" cy="15" r="11" fill="none" stroke="#fff" stroke-width="4"/><line x1="23" y1="23" x2="35" y2="35" stroke="#fff" stroke-width="5"/></svg>
  </div>
  <div class="thumb t2 abs" role="img" aria-label="Photo of a stone house with a round bay"></div>
  <div class="thumb t3 abs" role="img" aria-label="Photo of a brick wall with white windows"></div>
  <div class="thumb t4 abs" role="img" aria-label="Photo of an interior being plastered"></div>
</section>

<section class="video-band abs">
  <svg class="abs" style="left:0;top:0" width="1200" height="426" viewBox="0 0 1200 426">
    <defs><linearGradient id="wave" x1="0" y1="0" x2="0" y2="1"><stop offset="0" stop-color="#9fd5ec"/><stop offset=".4" stop-color="#6fb6de"/><stop offset="1" stop-color="#5aa8d8"/></linearGradient></defs>
    <path d="M0 80 Q600 -40 1200 80 V426 H0 Z" fill="url(#wave)"/>
  </svg>
  <h2 class="video-title abs">Watch Our Latest Video</h2>
  <p class="video-lead abs">Curabitur iaculis tempus eros Curabitur vel mi sit amet magna malesuada ultrices Ut nisi erat fermentum</p>
  <p class="video-body abs">congue id euismod in elit Fusce ultricies orci ac feugiat suscipit leo massa sodales velit et scelerisque mi tortor at ipsum cligula augue bibendum accumsan vestibulum ut commodo a mi Morbi ornare</p>
  <div class="player abs" role="img" aria-label="Video still of a plasterer skimming a ceiling">
    <svg class="abs" style="left:173px;top:86px" width="46" height="46" viewBox="0 0 46 46"><circle cx="23" cy="23" r="23" fill="#111"/><polygon points="18,13 34,23 18,33" fill="#fff"/></svg>
    <div class="player-bar abs">
      <svg width="398" height="26" viewBox="0 0 398 26"><polygon points="8,8 16,13 8,18" fill="#fff"/><rect x="26" y="11" width="260" height="4" fill="#fff"/><rect x="26" y="11" width="92" height="4" fill="#3a8fe0"/><polygon points="372,10 376,10 381,6 381,20 376,16 372,16" fill="#fff"/><path d="M385 9q4 4 0 8" fill="none" stroke="#fff" stroke-width="1.5"/></svg>
    </div>
  </div>
</section>

<section class="testimonials abs">
  <h2 class="test-title abs">Client Testimonials</h2>
  <div class="avatar abs" role="img" aria-label="Portrait photo of a smiling client"></div>
  <div class="quote-mark abs" style="left:414px;top:104px">&ldquo;</div>
  <p class="quote-text abs">Curabitur iaculis tempus eros Curabitur vel mi sit amet magna malesuada ultrices Ut nisi erat fermentum vel congue id euismod in elit Fusce ultricies orci ac feugiat suscipit leo massa sodales velit et scelerisque mi tortor at ipsum cligula augue</p>
  <div class="quote-mark abs" style="left:880px;top:180px">&rdquo;</div>
  <div class="quote-author abs">By Author Name</div>
  <div class="quote-city abs">City Location</div>
  <div class="dots abs"><span class="dot open"></span><span class="dot"></span><span class="dot"></span></div>
</section>

<footer class="site-footer abs">
  <div class="abs" style="left:158px;top:48px;width:250px">
    <div class="f-head">Latest Tweets</div>
    <div class="tweet" style="margin-top:16px"><strong>Vestibulum ligula</strong>@ inceptos hymenaeos<br>Curabitur metus ipsum luctus eu malesuada ut<br>2 days ago</div>
    <div class="tweet" style="margin-top:18px"><strong>Vestibulum ligula</strong>@ inceptos hymenaeos<br>Curabitur metus ipsum luctus eu malesuada ut<br>2 days ago</div>
  </div>
  <div class="abs" style="left:426px;top:48px">
    <div class="f-head">Information</div>
    <ul class="f-links" style="margin-top:8px"><li>Home</li><li>About Us</li><li>How We Work</li><li>Recent Work</li><li>Testimonials</li></ul>
  </div>
  <div class="abs" style="left:592px;top:48px">
    <div class="f-head">Get a Quote</div>
    <div style="margin-top:16px">
      <div class="f-field">Name</div>
      <div class="f-field">Email address</div>
      <div class="f-field">Phone</div>
      <div class="f-send">SEND</div>
    </div>
  </div>
  <div class="abs" style="left:853px;top:48px">
    <div class="f-head">Contact Info</div>
    <div style="margin-top:10px">
      <div class="contact-line">42 Millrace Court Suite B7</div>
      <div class="contact-line">Ashvale, PA 18990</div>
      <div class="contact-line big"><svg width="16" height="16" viewBox="0 0 24 24"><path d="M6.6 10.8a15 15 0 0 0 6.6 6.6l2.2-2.2a1 1 0 0 1 1-.25 11.4 11.4 0 0 0 3.6.57 1 1 0 0 1 1 1V20a1 1 0 0 1-1 1A17 17 0 0 1 3 4a1 1 0 0 1 1-1h3.5a1 1 0 0 1 1 1c0 1.25.2 2.45.57 3.57a1 1 0 0 1-.25 1z" fill="#fff"/></svg>(555) 309-4410</div>
      <div class="contact-line"><svg width="18" height="14" viewBox="0 0 18 14"><rect width="18" height="14" rx="1" fill="#fff"/><polyline points="1,1 9,8 17,1" fill="none" stroke="#0c3f86" stroke-width="1.6"/></svg>hello@hollowbrookrw.com</div>
      <div class="socials"><span class="social"></span><span class="social"></span><span class="social"></span><span class="social"></span></div>
    </div>
  </div>
  <div class="f-rule abs"></div>
  <div class="copyright abs">© 2016 Company Name &nbsp;All right reserved &nbsp;Term of Use</div>
</footer>

</body>
</html>
```